Postcard for Direct Mailing

I need a Postcard Design that could be used for a direct mailing campaign. I just started a company called BrightLedger (www.brightledger-example.com) which is an Administrating Consulting Services Company. It is basically a mix of being a Project Manager/Business Analysis/and Virtual Assistant.
My motto is "A Modern Solution to a Classic Problem"

The files that I attached I purchased from stock photos. and I would like them merged together for 1 side that shows how the problem with office staff has been forever.

Also the last one is my logo that should be on the side of the postcard where it can be sent out.

Below I have attached content. I'm not sure if it is too much.

Potential One Side
Are you losing time that could be better spent creating new business leads and focusing on the work at hand?
Worrying about the office work doesn't get it done …..
It may seem like modern technology would streamline your office processes to the point where you can do it all on your own without an assistance, but there is still only so much you can do to strike balance in the midst of running a thriving business.
That’s where BrightLedger Administrative Consulting Services steps in!

Potential Second Side
Let us take that load off your shoulders, while we assist with the taking over tasks that are cutting into your productivity. With the right assistance—or team—fighting on your behalf to create order, I act as another extension of your business and help you with your administrative support needs so that you can concentrate on what really matters – growing your business!
As a part of this customized service, we will take care of the following tasks:
• Word Processing
• Spreadsheet Creation/Tracking
• Research Services
• SlideCraft and other Presentations
• Database Management
• Data Entry
• Internet Research
• Client Relationship Management
• Email Management
• Calendar Management
• Conference Calls
• Vendor Management

Call today for further information, or to arrange a free consultation to determine which services we can provide for you call us at (800) 555-0143 or visit the site www.brightLEDGER-example.com TODAY!

```html
<!DOCTYPE html>
<html lang="en">
<head>
<meta charset="utf-8">
<title>BrightLedger Direct Mail Postcard</title>
<link href="https://fonts.googleapis.com/css2?family=Source+Sans+3:wght@400;600;700&display=swap" rel="stylesheet">
<style>
  :root {
    --backdrop: #1d1d1d;
    --paper: #ffffff;
    --ink: #1e1e1e;
    --navy: #1c2f7a;
    --blue-deep: #1f4fa0;
    --blue-mid: #2a6cc0;
    --blue-light: #4f9be0;
    --green: #2e9a46;
    --white: #ffffff;
    --stamp-line: #9a9a9a;
  }
  * { box-sizing: border-box; margin: 0; padding: 0; }
  html, body {
    width: 1200px; height: 1200px; overflow: hidden;
    background: var(--backdrop);
    font-family: "Source Sans 3", "Myriad Pro", sans-serif;
    color: var(--ink);
  }
  .canvas { position: relative; width: 1200px; height: 1200px; }

  /* Mailing side */
  .card-mail {
    position: absolute; left: 419px; top: 24px; width: 727px; height: 560px;
    background: var(--paper);
  }
  .mail-intro {
    position: absolute; left: 11px; top: 14px; width: 340px;
    font-size: 14.5px; line-height: 1.28; text-align: justify;
  }
  .service-panel {
    position: absolute; left: 0; top: 178px; width: 351px; height: 290px;
    background: radial-gradient(ellipse at 75% 45%, var(--blue-light) 0%, var(--blue-mid) 40%, var(--blue-deep) 100%);
    color: var(--white); padding: 10px 11px;
  }
  .service-panel h2 {
    font-size: 15px; font-weight: 700; line-height: 1.25; margin-bottom: 6px;
  }
  .service-list { list-style: none; padding-left: 14px; }
  .service-list li {
    font-size: 15px; line-height: 18.4px; position: relative; padding-left: 14px;
  }
  .service-list li::before {
    content: "•"; position: absolute; left: 0; top: 0;
  }
  .mail-call {
    position: absolute; left: 11px; top: 478px; width: 340px;
    font-size: 14.5px; line-height: 1.28;
  }
  .mail-call strong { color: var(--navy); font-weight: 700; }
  .mail-brand {
    position: absolute; left: 372px; top: 62px;
    display: flex; align-items: center; gap: 8px;
    font-size: 22px; font-weight: 700; color: var(--navy);
  }
  .brand-dot { width: 14px; height: 14px; border-radius: 50%; background: var(--green); flex: none; }
  .stamp-box {
    position: absolute; left: 550px; top: 12px; width: 166px; height: 166px;
    border: 1px solid var(--stamp-line);
  }

  /* Message side */
  .card-front {
    position: absolute; left: 64px; top: 614px; width: 729px; height: 562px;
    background: var(--navy); overflow: hidden;
  }
  .photo-history {
    position: absolute; left: 0; top: 0; width: 364px; height: 242px;
    background: linear-gradient(160deg, #8a8a8a, #4a4a4a 60%, #6c6c6c);
  }
  .photo-modern {
    position: absolute; left: 364px; top: 0; width: 365px; height: 242px;
    background: linear-gradient(160deg, #eeeeee, #c9c2bc 55%, #f2f2f2);
  }
  .question-band {
    position: absolute; left: 0; top: 242px; width: 729px; height: 88px;
    background: linear-gradient(90deg, var(--blue-deep), var(--blue-mid) 60%, var(--blue-deep));
    border-top: 2px solid var(--green); border-bottom: 2px solid var(--green);
    color: var(--white);
  }
  .question-band h1 {
    position: absolute; left: 10px; top: 10px; width: 660px;
    font-size: 27px; font-weight: 400; line-height: 1.2;
  }
  .question-mark {
    position: absolute; right: 12px; top: 0; font-size: 66px; line-height: 1; font-weight: 400;
  }
  .message-panel {
    position: absolute; left: 0; top: 330px; width: 729px; height: 232px;
    background: radial-gradient(ellipse at 40% 80%, var(--blue-light) 0%, var(--blue-mid) 35%, var(--navy) 100%);
  }
  .message-copy {
    position: absolute; left: 0; top: 14px; width: 477px; height: 196px;
    border-left: 9px solid var(--green); border-right: 1px solid rgba(255,255,255,0.35);
    padding: 0 12px 0 13px; color: var(--white);
  }
  .message-copy .lead { font-size: 16.5px; font-weight: 700; margin-bottom: 10px; }
  .message-copy p { font-size: 16.5px; line-height: 1.3; }
  .message-copy .close { font-weight: 700; margin-top: 12px; }
  .message-contact {
    position: absolute; left: 478px; top: 14px; width: 251px; height: 206px;
    border-right: 9px solid var(--green); color: var(--white); text-align: center;
    padding-right: 0;
  }
  .front-brand {
    margin-top: 48px; display: flex; justify-content: center; align-items: center; gap: 8px;
    font-size: 28px; font-weight: 700;
  }
  .front-brand .brand-dot { width: 16px; height: 16px; }
  .front-url {
    margin-top: 48px; font-size: 15.5px; line-height: 1.2; white-space: nowrap;
  }
  .front-phone { font-size: 30px; line-height: 1.15; white-space: nowrap; }
</style>
</head>
<body>
<div class="canvas">

  <section class="card-mail">
    <p class="mail-intro">Let us take that load off your shoulders, while we assist with the taking over tasks that are cutting into your productivity. With the right assistance—or team—fighting on your behalf to create order, I act as another extension of your business and help you with your administrative support needs so that you can concentrate on what really matters – growing your business!</p>
    <div class="service-panel">
      <h2>As a part of this customized service, we will take care of the following tasks:</h2>
      <ul class="service-list">
        <li>Word Processing</li>
        <li>Spreadsheet Creation/Tracking</li>
        <li>Research Services</li>
        <li>SlideCraft and other Presentations</li>
        <li>Database Management</li>
        <li>Data Entry</li>
        <li>Internet Research</li>
        <li>Client Relationship Management</li>
        <li>Email Management</li>
        <li>Calendar Management</li>
        <li>Conference Calls</li>
        <li>Vendor Management</li>
      </ul>
    </div>
    <p class="mail-call">Call today for further information, or to arrange a free consultation to determine which services we can provide for you call us at <strong>(800) 555-0143</strong> or visit the site <strong>www.brightLEDGER-example.com TODAY!</strong></p>
    <div class="mail-brand"><span class="brand-dot"></span>BrightLedger</div>
    <div class="stamp-box"></div>
  </section>

  <section class="card-front">
    <div class="photo-history" role="img" aria-label="Black and white photograph of a 1920s office team gathered around a desk of paperwork"></div>
    <div class="photo-modern" role="img" aria-label="Color photograph of three stressed modern office workers at a table"></div>
    <div class="question-band">
      <h1>Are you losing time that could be better spent creating new business leads and focusing on the work at hand</h1>
      <span class="question-mark">?</span>
    </div>
    <div class="message-panel">
      <div class="message-copy">
        <p class="lead">Worrying about the office work doesn't get it done …..</p>
        <p>It may seem like modern technology would streamline your office processes to the point where you can do it all on your own without an assistance, but there is still only so much you can do to strike balance in the midst of running a thriving business.</p>
        <p class="close">That’s where BrightLedger Administrative Consulting Services steps in!</p>
      </div>
      <div class="message-contact">
        <div class="front-brand"><span class="brand-dot"></span>BrightLedger</div>
        <div class="front-url">www.brightLEDGER-example.com</div>
        <div class="front-phone">(800) 555-0143</div>
      </div>
    </div>
  </section>

</div>
</body>
</html>
```